New Artwork/Design for Established Weight Loss Podcast

Hello,
I would like new artwork/design for my podcast. It's called Bright Path Slimdown and has been a consistently top 50 show in the fitness/nutrition category on Orbix. My current design was originally created when I started the podcast over 2 years ago. It's time to refresh and update things! I would like a new design that incorporates a photo of me, but could also be used as a standalone logo for the podcast without my photo. A nice, clean, professional, yet fun design. Here is a Vantor drive link with professional photos that could be used:
https://files.example-share.net/folders/7Qkrt58x-p2mLWHtabvPXsaQ9Ro6JwZ3k?usp=sharing

Here's a little more about the show . There are three big taglines. These do NOT need to be included on the design. I just include them here to help with the feel/theme of the design.

1: To change your body, you must first change your brain.
2: There's so much more to you than just a number (what you weigh).
3: Losing weight is really about gaining life and living the life you've always wanted.

This podcast is all about busy moms, dads, husbands, wives who are working, raising kids, and trying to juggle everything life’s throwing at them … but also want to be the best they can for their family and friends and loved ones.

The podcast is NOT about how to get six-pack abs or how to drop as much weight as possible in 8 weeks. It's about finding sustainable success with your body, peace of mind with food, and improving your relationship with yourself.

Week by week, I provide bite-sized guidance - 20-25 minute episodes that pull back the curtain and reveal the truth about what it takes to lose weight and gain life - what strategy and approach real people are using to get results while escaping the soul-sucking, all-or-nothing diet mentality.

Here's a link to the current artwork: https://files.example-share.net/file/d/4T2bHn8qsvkeTrmzYpRd-ab3KNJ-m-QXZ/view?usp=sharing

And the logo without my photo: https://files.example-share.net/file/d/8JN5pKa3Rw_h2b74cFxYqPmE6zGtdLs/view?usp=sharing

I'm open to any colors, but something that either matches the colors of my website or signature "Move Glow Trim Down" program would probably be a smart idea. Here are links to my website and the MGTD logo . . .

Website: https://danemarshwellness.example/

MGTD logo:
https://files.example-share.net/file/d/5VQpLm2Kxe_Tw9Hr4zNgUa7YcBfsjdP/view?usp=sharing

Happy to answer any questions you might have. Thanks.

Target Market(s)

35 to 55 years old, roughly 70% female, 30% male, professionals, primarily in the U.S. and Canada

Industry/Entity Type

nutrition, health, weight loss

Requirements
Must have
• One version with my photo and the same design without my photo
Nice to have
• Open to any colors, but possibly incorporate colors from either my website or MGTD logo (see project description for more info)
Should not have
• Any hardcore fitness or bodybuilding imagery

```html
<!DOCTYPE html>
<html lang="en">
<head>
<meta charset="utf-8">
<title>Bright Path Slimdown – Podcast Cover Set</title>
<link rel="stylesheet" href="https://fonts.googleapis.com/css2?family=Archivo:wght@300;700;800&family=Mrs+Saint+Delafield&display=swap">
<style>
  :root {
    --stage: #dcdcdc;
    --teal: #63ada9;
    --teal-line: #5fb0ad;
    --charcoal: #3d3d40;
    --white: #ffffff;
    --photo-top: #8a8f9c;
    --photo-bottom: #b9c3dc;
  }
  * { margin: 0; padding: 0; box-sizing: border-box; }
  html, body {
    width: 1200px; height: 618px; overflow: hidden;
    background: var(--stage);
    font-family: "Archivo", Arial, sans-serif;
  }
  .cover {
    position: absolute; top: 36px;
    width: 554px; height: 554px;
    background: var(--teal);
    overflow: hidden;
    box-shadow: 0 2px 5px rgba(0,0,0,.25);
  }
  .cover--photo { left: 37px; }
  .cover--logo { left: 610px; }
  .band { position: absolute; inset: 0; width: 554px; height: 554px; }
  .host-photo { position: absolute; inset: 0; width: 554px; height: 554px; }
  .title {
    position: absolute;
    z-index: 2;
    color: var(--white);
    font-weight: 800;
    text-transform: uppercase;
    letter-spacing: -1px;
  }
  .cover--photo .title {
    left: 36px; top: 34px;
    font-size: 58px; line-height: 64px;
  }
  .cover--logo .title {
    left: 0; right: 0; top: 22px;
    text-align: center;
    font-size: 104px; line-height: 84px;
  }
  .label {
    position: absolute;
    z-index: 2;
    color: var(--white);
    font-weight: 700;
    font-size: 21px;
  }
  .host {
    position: absolute;
    z-index: 2;
    color: var(--white);
    font-weight: 700;
    font-size: 36px;
    letter-spacing: -0.5px;
    white-space: nowrap;
  }
  .host__with {
    font-family: "Mrs Saint Delafield", cursive;
    font-weight: 400;
    font-size: 34px;
    letter-spacing: 0;
  }
  .brand {
    position: absolute;
    z-index: 2;
    display: flex; align-items: center; gap: 12px;
  }
  .brand__mark {
    width: 34px; height: 34px;
    border: 1.5px solid var(--teal-line);
  }
  .brand__name {
    color: var(--white);
    font-weight: 300;
    font-size: 13px;
    letter-spacing: 3px;
    line-height: 17px;
    text-transform: uppercase;
  }
</style>
</head>
<body>

<section class="cover cover--photo">
  <svg class="band" viewBox="0 0 554 554" aria-hidden="true">
    <polygon points="0,392 120,350 250,250 554,150 554,554 0,554" fill="var(--charcoal)"/>
  </svg>
  <svg class="host-photo" viewBox="0 0 554 554" role="img" aria-label="Portrait photo of the host in a light blue shirt with arms crossed">
    <defs>
      <linearGradient id="photoTone" x1="0" y1="0" x2="0" y2="1">
        <stop offset="0" stop-color="var(--photo-top)"/>
        <stop offset="0.4" stop-color="var(--photo-bottom)"/>
        <stop offset="1" stop-color="var(--photo-bottom)"/>
      </linearGradient>
    </defs>
    <path d="M398,100 Q398,34 452,34 Q508,34 508,100 L508,215 Q530,232 554,250 L554,554 L290,554 Q262,420 262,330 Q262,272 330,250 Q380,232 398,215 Z" fill="url(#photoTone)"/>
  </svg>
  <h1 class="title">Bright<br>Path<br>Slimdown</h1>
  <div class="label" style="left:36px; top:256px;">Podcast</div>
  <div class="host" style="left:40px; top:420px;">
    <span class="host__with" style="display:block; margin-left:70px; line-height:28px;">with</span>
    Dane Marsh
  </div>
  <div class="brand" style="left:40px; top:503px;">
    <span class="brand__mark"></span>
    <span class="brand__name">Move Glow<br>Trim Down</span>
  </div>
</section>

<section class="cover cover--logo">
  <svg class="band" viewBox="0 0 554 554" aria-hidden="true">
    <polygon points="0,402 150,370 300,345 430,335 554,410 554,554 0,554" fill="var(--charcoal)"/>
  </svg>
  <h1 class="title">Bright<br>Path<br>Slim<br>Down</h1>
  <div class="label" style="left:0; right:0; top:382px; text-align:center;">Podcast</div>
  <div class="host" style="left:0; right:0; top:428px; text-align:center;">
    <span class="host__with">with</span> Dane Marsh
  </div>
  <div class="brand" style="left:208px; top:503px;">
    <span class="brand__mark"></span>
    <span class="brand__name">Move Glow<br>Trim Down</span>
  </div>
</section>

</body>
</html>
```